Business Card Design

I need a business card design for a new company based in Australind, Western Australia. The business is for puppet shows at children's parties, fetes, custom puppet builds, etc.Attached is a picture of Ray Pellow in silhouette. I was thinking a design of a puppeteer at the top of some stairs talking to a puppet in silhouette but open to suggestions. (Lantern Loft is named as I do all my puppet builds in the top room of my house (at the Lantern Loft).

Industry/Entity Type

Business

Contact Information for Business Card

Lantern Loft Marionettes, Dale Voss, Puppeteer / Puppet Builder, phone - 0438562703, Puppet shows / Custom Puppet Builds, Working With Children

Requirements
Must have
• Name and Logo on one side. Second side to have business card details.

```html
<!DOCTYPE html>
<html lang="en">
<head>
<meta charset="utf-8">
<title>Lantern Loft Marionettes – Business Card</title>
<link href="https://fonts.googleapis.com/css2?family=Arimo:wght@400;700&family=Chewy&display=swap" rel="stylesheet">
<style>
  :root {
    --page-bg: #161616;
    --card-white: #ffffff;
    --band-black: #000000;
    --card-blue: #3b72b4;
    --text-dark: #000000;
    --text-light: #ffffff;
    --strip-a: #e8c9a4;
    --strip-b: #b8c3d8;
    --strip-c: #e7d46a;
  }
  * { margin: 0; padding: 0; box-sizing: border-box; }
  html, body {
    width: 1189px; height: 1200px; overflow: hidden;
    background: var(--page-bg);
  }
  .canvas { position: relative; width: 1189px; height: 1200px; }
  .card {
    position: absolute; left: 140px; width: 917px; height: 524px;
    background: var(--card-white);
    box-shadow: 0 6px 18px rgba(0,0,0,.6);
  }
  .card--front { top: 45px; }
  .card--back { top: 623px; }
  .brand-title {
    position: absolute; left: 0; right: 0; top: 62px;
    text-align: center;
    font-family: "Chewy", cursive;
    font-size: 76px; line-height: 1; color: var(--text-dark);
    letter-spacing: -1px;
  }
  .character-strip {
    position: absolute; left: 0; top: 141px; width: 917px; height: 150px;
    background: linear-gradient(90deg, var(--strip-a), var(--strip-b) 30%, var(--strip-c) 50%, var(--strip-b) 70%, var(--strip-a));
    opacity: .85;
  }
  .band { position: absolute; left: 0; top: 291px; width: 917px; height: 33px; background: var(--band-black); }
  .info-panel {
    position: absolute; left: 0; top: 324px; width: 917px; height: 200px;
    background: var(--card-blue);
    font-family: "Arimo", Arial, sans-serif; color: var(--text-light);
  }
  .contact-name { position: absolute; left: 33px; top: 28px; font-size: 50px; line-height: 1; }
  .contact-role { position: absolute; left: 33px; top: 74px; font-size: 30px; line-height: 1; }
  .contact-phone { position: absolute; left: 33px; top: 126px; font-size: 30px; line-height: 1; font-weight: 700; letter-spacing: 1px; }
  .divider { position: absolute; left: 502px; top: 16px; width: 3px; height: 154px; background: var(--text-light); }
  .services { list-style: none; position: absolute; left: 528px; top: 28px; }
  .services li {
    display: flex; align-items: center; height: 47px;
    font-size: 31px; line-height: 1;
  }
  .services svg { width: 26px; height: 26px; margin-right: 18px; flex: none; }
</style>
</head>
<body>
<div class="canvas">
  <section class="card card--front">
    <h1 class="brand-title">Lantern Loft Marionettes</h1>
    <div class="character-strip" role="img" aria-label="Row of colourful puppet characters"></div>
    <div class="band"></div>
    <div class="info-panel">
      <p class="contact-name">Dale Voss</p>
      <p class="contact-role">Puppeteer / Puppet Builder</p>
      <p class="contact-phone">0438562703</p>
      <div class="divider"></div>
      <ul class="services">
        <li><svg viewBox="0 0 26 26"><circle cx="13" cy="13" r="8" fill="none" stroke="#fff" stroke-width="1.5"/><circle cx="13" cy="13" r="3" fill="#fff"/><path d="M13 1v6M13 19v6M1 13h6M19 13h6" stroke="#fff" stroke-width="1.5"/></svg>Puppet shows</li>
        <li><svg viewBox="0 0 26 26"><circle cx="13" cy="13" r="8" fill="none" stroke="#fff" stroke-width="1.5"/><circle cx="13" cy="13" r="3" fill="#fff"/><path d="M13 1v6M13 19v6M1 13h6M19 13h6" stroke="#fff" stroke-width="1.5"/></svg>Custom Puppet Builds</li>
        <li><svg viewBox="0 0 26 26"><circle cx="13" cy="13" r="8" fill="none" stroke="#fff" stroke-width="1.5"/><circle cx="13" cy="13" r="3" fill="#fff"/><path d="M13 1v6M13 19v6M1 13h6M19 13h6" stroke="#fff" stroke-width="1.5"/></svg>Working With Children</li>
      </ul>
    </div>
  </section>

  <section class="card card--back">
    <h1 class="brand-title">Lantern Loft Marionettes</h1>
    <div class="character-strip" role="img" aria-label="Row of colourful puppet characters"></div>
    <div class="band"></div>
    <div class="info-panel">
      <p class="contact-name">Dale Voss</p>
      <p class="contact-role">Puppeteer / Puppet Builder</p>
      <p class="contact-phone">0438562703</p>
      <div class="divider"></div>
      <ul class="services">
        <li><svg viewBox="0 0 26 26"><circle cx="13" cy="13" r="8" fill="none" stroke="#fff" stroke-width="1.5"/><circle cx="13" cy="13" r="3" fill="#fff"/><path d="M13 1v6M13 19v6M1 13h6M19 13h6" stroke="#fff" stroke-width="1.5"/></svg>Puppet shows</li>
        <li><svg viewBox="0 0 26 26"><circle cx="13" cy="13" r="8" fill="none" stroke="#fff" stroke-width="1.5"/><circle cx="13" cy="13" r="3" fill="#fff"/><path d="M13 1v6M13 19v6M1 13h6M19 13h6" stroke="#fff" stroke-width="1.5"/></svg>Custom Puppet Builds</li>
        <li><svg viewBox="0 0 26 26"><circle cx="13" cy="13" r="8" fill="none" stroke="#fff" stroke-width="1.5"/><circle cx="13" cy="13" r="3" fill="#fff"/><path d="M13 1v6M13 19v6M1 13h6M19 13h6" stroke="#fff" stroke-width="1.5"/></svg>Working With Children</li>
      </ul>
    </div>
  </section>
</div>
</body>
</html>
```